Book cover for a very impressive real-life healing story from a stage IV deadly disease

I need a book cover design for the French translation of the US book http://www.pagevendo.com/Tims-Journey-Fever-Outlasted-Illness/dp/0845512097/ref=sr_1_4?s=books&ie=UTF8&qid=1455100794&sr=1-4&keywords=kit+marsh
.
I do not want the word AIDS on the French cover, as the story of this book applies to any disease.

The french title will be something like :
Un nouveau matin !
Condamné par la médecine, il guérit grâce au jeûne, la détoxination, et l’amour.

which means something like
A new morning!
Subtitle : Given up by official medecine, he managed to heal with fasting, detox and love.

Many thanks !

Target Market(s)

Anybody interested in natural health

Requirements
Must have
• Nothing special
Nice to have
• Nothing special
Should not have
• Nothing special

```html
<!DOCTYPE html>
<html lang="fr">
<head>
<meta charset="utf-8">
<title>Un nouveau matin !</title>
<link rel="stylesheet" href="https://fonts.googleapis.com/css2?family=Anton&family=Oswald:wght@700&family=Arimo&display=swap">
<style>
  :root {
    --ink: #000000;
    --red: #d5242b;
    --white: #ffffff;
    --flame-hot: #f6e9a8;
    --flame-mid: #e49a2c;
    --ember: #6b2a14;
  }
  html, body { margin: 0; padding: 0; overflow: hidden; background: var(--ink); }
  .cover {
    position: relative;
    width: 750px;
    height: 1200px;
    background: var(--ink);
    overflow: hidden;
  }
  .title-line {
    position: absolute;
    left: 44px;
    margin: 0;
    font-family: "Anton", "Oswald", sans-serif;
    font-weight: 400;
    color: var(--red);
    line-height: 1;
    white-space: nowrap;
    transform-origin: left top;
  }
  .title-line--first {
    top: 63px;
    font-size: 149px;
    transform: scaleY(1.39);
  }
  .title-line--second {
    top: 282px;
    font-size: 175px;
    transform: scaleY(1.26);
  }
  .subtitle {
    position: absolute;
    left: 565px;
    top: 288px;
    margin: 0;
    font-family: "Oswald", sans-serif;
    font-weight: 700;
    font-size: 19px;
    line-height: 30px;
    color: var(--red);
    text-transform: uppercase;
    letter-spacing: -0.2px;
  }
  .rule {
    position: absolute;
    left: 0;
    top: 525px;
    width: 750px;
    height: 6px;
    background: var(--red);
  }
  .author {
    position: absolute;
    left: 42px;
    top: 550px;
    margin: 0;
    font-family: "Arimo", Arial, sans-serif;
    font-size: 44px;
    color: var(--white);
  }
  .emblem {
    position: absolute;
    left: 230px;
    top: 635px;
    width: 290px;
    height: 282px;
    background: radial-gradient(ellipse at center, rgba(213,36,43,0.35), rgba(213,36,43,0) 70%);
  }
  .fire {
    position: absolute;
    left: 0;
    top: 930px;
    width: 750px;
    height: 270px;
    background:
      radial-gradient(ellipse 60% 70% at 35% 75%, var(--flame-hot), rgba(228,154,44,0) 70%),
      linear-gradient(to bottom, var(--ink) 0%, var(--flame-mid) 45%, var(--ember) 100%);
  }
</style>
</head>
<body>
  <main class="cover">
    <h1 class="title-line title-line--first">UN NOUVEAU</h1>
    <p class="title-line title-line--second">MATIN !</p>
    <p class="subtitle">Condamné par<br>la médecine, il<br>guérit grâce<br>au jeûne,<br>la détoxination,<br>et l’amour</p>
    <div class="rule"></div>
    <p class="author">Kit Marsh</p>
    <div class="emblem" role="img" aria-label="Red outline emblem of a phoenix with spread wings"></div>
    <div class="fire" role="img" aria-label="Photograph of burning logs and flames"></div>
  </main>
</body>
</html>
```